HARVEST sales brochure

Our company, MedSparrowGrove, has recently undertaken a re-branding overhaul to change our website and corporate materials (color scheme, letterhead, biz cards). In support of this re-branding effort, we need an initial sales brochure designed for our company's services that will reflect the look and feel of the website. The website design, fonts and images are included as attachments for your reference.

The brochure will be distributed primarily via email. The audience will be prospective buyers - generally pharmaceutical companies or smaller biotech companies, either of whom are developing treatments for different diseases.

Attached is a word document which contains the text for the brochure. The powerpoint document titled 'case studies' provides example charts and graphs that can be used.
We would like a final format in a layered PSD (photoshop file).

A modular brochure that would allow us to include one or more case studies based on the sales opportunity would be a plus.
Updates

Attention: The text for the brochure has been updated.

Target Market(s)

Pharmaceutical companies / biotechnology companies

Industry/Entity Type

Pharmaceutical

Requirements
Must have
• Utilize the images we have provided as attachments where possible. And choose from our color palette and fonts.
Nice to have
• Additional graphics that reflect the look and feel per our attachments.

```html
<!DOCTYPE html>
<html lang="en">
<head>
<meta charset="utf-8">
<title>MedSparrowGrove HARVEST Brochure</title>
<link href="https://fonts.googleapis.com/css2?family=Mulish:wght@400;600;700;800&display=swap" rel="stylesheet">
<style>
  :root {
    --ink: #000000;
    --brand-blue: #22aadb;
    --heading-blue: #1ea3d7;
    --charcoal: #4b4b50;
    --band: #4d4d52;
    --paper: #ffffff;
    --butter: #fbdc80;
    --logo-cream: #f3d57c;
    --sky: #a6dcf4;
    --orange: #f8a826;
  }
  * { box-sizing: border-box; margin: 0; padding: 0; }
  html, body {
    width: 1200px; height: 814px; overflow: hidden;
    background: var(--ink);
    font-family: "Mulish", "Helvetica Neue", Arial, sans-serif;
    color: var(--charcoal);
  }
  .spread { position: relative; width: 1200px; height: 814px; }
  .page {
    position: absolute; width: 571px; background: var(--paper); overflow: hidden;
  }
  .page--cover { left: 21px; top: 21px; height: 378px; background: var(--brand-blue); }
  .page--about { left: 608px; top: 21px; height: 378px; }
  .page--platform { left: 21px; top: 416px; height: 379px; }
  .page--mission { left: 608px; top: 416px; height: 379px; }

  .footer-band {
    position: absolute; left: 0; right: 0; bottom: 0; height: 69px;
    background: var(--band);
  }
  .wordmark {
    font-weight: 400; color: var(--logo-cream); letter-spacing: 0.01em;
  }
  .footer-band .wordmark {
    position: absolute; right: 40px; top: 24px; font-size: 16px;
  }
  .cover-wordmark {
    position: absolute; left: 0; right: 0; top: 202px; text-align: center;
    font-size: 38px; color: var(--charcoal);
  }

  .flask-art {
    position: absolute; left: 0; top: 20px; width: 222px; height: 358px;
    background: linear-gradient(180deg, #ffffff 0%, var(--sky) 55%, #8fd2ef 100%);
    border-radius: 0 0 30px 0;
  }
  .about-copy { position: absolute; left: 244px; top: 99px; width: 290px; }
  .title {
    font-weight: 800; text-transform: uppercase; color: var(--heading-blue);
    font-size: 28px; line-height: 1.08; letter-spacing: 0.01em;
  }
  .about-copy p { margin-top: 8px; font-size: 14px; line-height: 1.25; }

  .person-art {
    position: absolute; left: 0; top: 28px; width: 252px; height: 351px;
    background: linear-gradient(180deg, #fbb744 0%, var(--orange) 100%);
    border-radius: 120px 120px 0 0;
  }
  .platform-copy { position: absolute; left: 272px; top: 40px; width: 270px; }
  .platform-copy h2 {
    font-weight: 800; font-size: 22px; line-height: 1.05; color: var(--charcoal);
  }
  .platform-copy p {
    margin-top: 6px; font-size: 10.8px; line-height: 15.5px; letter-spacing: -0.1px;
  }
  .platform-copy p + p { margin-top: 8px; }

  .page--mission .title { position: absolute; left: 0; right: 0; top: 34px; text-align: center; }
  .column {
    position: absolute; top: 74px; font-size: 10px; line-height: 13.6px; letter-spacing: -0.1px;
  }
  .column h3 { font-size: 11.5px; font-weight: 800; line-height: 13.6px; margin-bottom: 8px; }
  .column--need { left: 38px; width: 174px; }
  .column--cost { left: 226px; width: 146px; }
  .column--cost h3 { margin-bottom: 2px; }
  .callout {
    left: 383px; width: 152px; height: 218px; background: var(--butter);
    padding: 14px 13px;
  }
  .callout h3 { margin-bottom: 8px; }
</style>
</head>
<body>
<main class="spread">

  <section class="page page--cover">
    <div class="wordmark cover-wordmark">MedSparrowGrove™</div>
  </section>

  <section class="page page--about">
    <div class="footer-band"><span class="wordmark">MedSparrowGrove™</span></div>
    <div class="flask-art" role="img" aria-label="Illustration of a laboratory flask filled with light blue liquid and rising bubbles"></div>
    <div class="about-copy">
      <h1 class="title">What we do exactly</h1>
      <p>We’re MedSparrowGrove, a place where people can share and access medical data to hasten the search for cures.</p>
    </div>
  </section>

  <section class="page page--platform">
    <div class="footer-band"><span class="wordmark">MedSparrowGrove™</span></div>
    <div class="person-art" role="img" aria-label="Illustration of an orange head-and-shoulders silhouette of a patient"></div>
    <div class="platform-copy">
      <h2>MedSparrowGrove<br>HARVEST</h2>
      <p>We’ve pioneered the HARVEST registry platform, which allows patients around the world to join others in reporting their own experience of disease. We collect and safeguard the data to protect patients’ privacy. We then upload the de-identified data to a common hub and share it with researchers and advocates.</p>
      <p>Our system helps researchers unlock more effective treatments. It helps care providers better understand diseases. It makes organizing patient communities easier for advocacy groups. And it lets patients see how other people are managing illness.</p>
    </div>
  </section>

  <section class="page page--mission">
    <div class="footer-band"><span class="wordmark">MedSparrowGrove™</span></div>
    <h1 class="title">Why we’re here</h1>
    <div class="column column--need">
      <h3>Every disease community should have a common, accessible patient registry.</h3>
      <p>We’ve heard over and over that creating a shared registry of patients is one of the most valuable things a disease community can do. A registry puts critical information about a disease all in one place. This makes it easier for researchers to study the disease, for patients to learn about front-line treatments and for advocates to speak on behalf of the disease community.</p>
    </div>
    <div class="column column--cost">
      <h3>But registries are hard to maintain.</h3>
      <p>Registries are expensive. They need constant upkeep—usually by people with a lot of expertise in disease and data management. Often there are multiple competing registries for one disease, which leads to siloed, dead-end data that nobody can use.</p>
    </div>
    <div class="column callout">
      <h3>MedSparrowGrove is here to fix all of that.</h3>
      <p>Our HARVEST platform enables anyone—from individual patients to global research organizations—to collect and share disease data in a way that’s controlled, transparent and centered on patients’ best interests.</p>
    </div>
  </section>

</main>
</body>
</html>
```